Generic Business Card

I need a business card for my new cafe which is only six weeks old. I'm continuously asked for a business so that customers can either keep or pass on to a friend. I'd also like a card that I can give out with each bill which contains the business name, address, contact details and website.
The cafe's internal design has an industrial feel to it with modern subdued colours. I have attached an internal photo along with my main hero shot and logo.
The hero shot features prominently on my website and other print material and I would also like it to appear on my bus card.

Target Market(s)

Men & women between 35 and 45 years of age who know and enjoy good coffee.

Industry/Entity Type

Industrial

Contact Information for Business Card

Shop 7b/318-320 Pellmore Road, East Caldervale 3187
Tel. 9642 3715
www.tolvana.com.au

```html
<!DOCTYPE html>
<html lang="en">
<head>
<meta charset="utf-8">
<title>Tolvana – Business Card</title>
<link rel="stylesheet" href="https://fonts.googleapis.com/css2?family=Open+Sans:wght@600;700;800&display=swap">
<style>
  :root {
    --page: #141414;
    --ink: #000000;
    --paper: #ffffff;
    --photo-dark: #1c1c1c;
    --photo-mid: #6a6a6a;
    --photo-light: #bdbdbd;
    --rule: #0c0c0c;
  }
  html, body {
    margin: 0;
    padding: 0;
    width: 1200px;
    height: 741px;
    overflow: hidden;
    background: var(--page);
  }
  .card {
    position: absolute;
    left: 80px;
    top: 82px;
    width: 1040px;
    height: 575px;
    overflow: hidden;
    font-family: "Open Sans", Arial, sans-serif;
    color: var(--paper);
  }
  .hero-photo {
    position: absolute;
    inset: 0;
    background:
      radial-gradient(ellipse 420px 300px at 820px 360px, var(--photo-light), transparent 70%),
      radial-gradient(ellipse 380px 220px at 360px 420px, #8a8a8a, transparent 75%),
      linear-gradient(100deg, var(--photo-dark) 0%, var(--photo-mid) 45%, #9a9a9a 70%, #4a4a4a 100%);
  }
  .thin-rule {
    position: absolute;
    left: 32px;
    right: 33px;
    height: 1px;
    background: var(--rule);
  }
  .thin-rule.top { top: 34px; }
  .thin-rule.bottom { top: 359px; }
  .brand-name {
    position: absolute;
    left: 0;
    right: 0;
    top: 82px;
    text-align: center;
    margin: 0;
    font-size: 128px;
    font-weight: 800;
    letter-spacing: 6px;
    line-height: 1;
    color: var(--paper);
  }
  .contact-band {
    position: absolute;
    left: 0;
    right: 0;
    top: 417px;
    height: 46px;
    background: var(--ink);
    border-top: 2px solid var(--paper);
    border-bottom: 2px solid var(--paper);
    box-shadow: 0 -4px 0 var(--ink), 0 4px 0 var(--ink);
  }
  .contact-icon {
    position: absolute;
    top: 401px;
    width: 78px;
    height: 78px;
    margin-left: -39px;
    border-radius: 50%;
    background: var(--ink);
    display: flex;
    align-items: center;
    justify-content: center;
  }
  .contact-icon svg { width: 44px; height: 44px; }
  .contact-text {
    position: absolute;
    top: 500px;
    width: 400px;
    margin-left: -200px;
    text-align: center;
    font-size: 20px;
    font-weight: 700;
    line-height: 33px;
  }
  .address { left: 191px; }
  .phone { left: 519px; }
  .web { left: 846px; }
</style>
</head>
<body>
  <div class="card">
    <div class="hero-photo" role="img" aria-label="Black and white photo of a barista pouring espresso from a coffee machine into a cup"></div>

    <div class="thin-rule top"></div>
    <h1 class="brand-name">TOLVANA</h1>
    <div class="thin-rule bottom"></div>

    <div class="contact-band"></div>

    <div class="contact-icon" style="left:191px">
      <svg viewBox="0 0 44 44" aria-hidden="true">
        <path d="M22 6 L4 22 L9 22 L9 38 L18 38 L18 28 L26 28 L26 38 L35 38 L35 22 L40 22 Z" fill="#fff"/>
        <path d="M22 11 L9 22.5" stroke="#000" stroke-width="2" fill="none"/>
        <path d="M22 11 L35 22.5" stroke="#000" stroke-width="2" fill="none"/>
      </svg>
    </div>
    <div class="contact-icon" style="left:519px">
      <svg viewBox="0 0 44 44" aria-hidden="true">
        <path d="M4 16 Q4 8 22 8 Q40 8 40 16 L40 19 L32 19 L32 14 L12 14 L12 19 L4 19 Z" fill="#fff"/>
        <path d="M13 17 L31 17 L38 36 L6 36 Z" fill="#fff"/>
        <g fill="#000">
          <circle cx="16" cy="24" r="1.8"/><circle cx="22" cy="24" r="1.8"/><circle cx="28" cy="24" r="1.8"/>
          <circle cx="15" cy="29" r="1.8"/><circle cx="22" cy="29" r="1.8"/><circle cx="29" cy="29" r="1.8"/>
        </g>
      </svg>
    </div>
    <div class="contact-icon" style="left:846px">
      <svg viewBox="0 0 44 44" aria-hidden="true" fill="none" stroke="#fff" stroke-width="2.6">
        <circle cx="22" cy="22" r="17"/>
        <ellipse cx="22" cy="22" rx="7.5" ry="17"/>
        <line x1="22" y1="5" x2="22" y2="39"/>
        <line x1="5" y1="22" x2="39" y2="22"/>
        <path d="M8 13 H36 M8 31 H36"/>
      </svg>
    </div>

    <div class="contact-text address">Shop 7b/318-320 Pellmore Road,<br>East Caldervale 3187</div>
    <div class="contact-text phone">9642 3715</div>
    <div class="contact-text web">www.tolvana.com.au</div>
  </div>
</body>
</html>
```